Property restoration company needs 'Appreciation Packet' to send customers

Need 3 items designed.
- a branded 'Thank You' greeting card. 4"x6" fold over style. Should look professional and match our brand identity. I would like to be able to get these printed with a specific message inside and also as blank-inside cards to hand write custom messages into.

Business is owned by a father and son. The thank you message in the card will be signed from both of us. I would like to add our pictures inside the card under the message to give it a personal feeling.

- a card requesting google reviews with a QR code linked to review form. Business card sized when printed. Front & Back printing.

- an information card explaining that we pay referral fees. Business card sized. Front & Back printing

```html
<!DOCTYPE html>
<html lang="en">
<head>
<meta charset="UTF-8">
<title>Thank You Card – Front</title>
<link href="https://fonts.googleapis.com/css2?family=Roboto:wght@700;900&display=swap" rel="stylesheet">
<style>
  :root {
    --page-bg: #f4f5f6;
    --card-top: #f8f8f6;
    --card-bottom: #ebe9e5;
    --headline-blue: #4ab3e2;
    --brand-blue: #1ba8dc;
    --wave-light: #bcd8ea;
    --wave-dark: #86c2e8;
  }
  * { margin: 0; padding: 0; box-sizing: border-box; }
  html, body {
    width: 1200px;
    height: 720px;
    overflow: hidden;
    background: var(--page-bg);
  }
  .canvas {
    position: relative;
    width: 1200px;
    height: 720px;
    display: flex;
    align-items: center;
    justify-content: center;
  }
  .card-front {
    position: relative;
    width: 400px;
    height: 600px;
    background: linear-gradient(180deg, var(--card-top), var(--card-bottom));
    overflow: hidden;
    box-shadow: 0 2px 10px rgba(0,0,0,0.08);
    font-family: "Roboto", Arial, sans-serif;
  }
  .headline {
    position: absolute;
    top: 96px;
    left: 0;
    right: 0;
    text-align: center;
    color: var(--headline-blue);
    font-weight: 900;
    line-height: 0.95;
    letter-spacing: -1px;
  }
  .headline-main { display: block; font-size: 84px; }
  .headline-sub { display: block; font-size: 60px; margin-top: 8px; }
  .brand {
    position: absolute;
    top: 318px;
    left: 0;
    right: 0;
    display: flex;
    align-items: center;
    justify-content: center;
    gap: 14px;
  }
  .brand-mark {
    width: 40px;
    height: 40px;
    border-radius: 50%;
    background: var(--brand-blue);
  }
  .brand-name {
    color: var(--brand-blue);
    font-weight: 900;
    font-size: 38px;
    line-height: 0.95;
    text-transform: uppercase;
    letter-spacing: -0.5px;
  }
  .waves {
    position: absolute;
    left: 0;
    bottom: 0;
    width: 400px;
    height: 600px;
  }
</style>
</head>
<body>
  <main class="canvas">
    <section class="card-front">
      <svg class="waves" viewBox="0 0 400 600" aria-hidden="true">
        <path d="M0 505 C150 495 300 440 400 345 L400 600 L0 600 Z" fill="var(--wave-light)" opacity="0.85"/>
        <path d="M40 600 C180 560 310 480 400 385 L400 600 Z" fill="var(--wave-dark)"/>
      </svg>
      <h1 class="headline">
        <span class="headline-main">THANK</span>
        <span class="headline-sub">YOU</span>
      </h1>
      <div class="brand">
        <span class="brand-name">Harbor<br>Restore</span>
        <span class="brand-mark"></span>
      </div>
    </section>
  </main>
</body>
</html>
```